Workbook Cover Design

I am needing the cover for a workbook designed. I have attached a sample cover along with a few images giving an idea what at I am looking for. I'm open to new color schemes. I also attached a flyer of the event to give you an idea of the current color theme. The workbook will be approximately 8.5 x 11.

Title : Stewardship Workshop 202
Lorna Pell Ministries

On the cover I would like to have four sections with the following title under each section:
Evangelism (use photo similar to hands with cross)
Praying in Tongues (Photo similar to bird with heart or one with a mouth speaking)
Authority of the Believer (Photo with badge or similar)
Healing (Photo of man and wheelchair or similar)

Using silhouettes are okay, but I prefer not to have any actual faces of people.

```html
<!DOCTYPE html>
<html lang="en">
<head>
<meta charset="utf-8">
<title>Stewardship Workshop 202 — Workbook Cover</title>
<link href="https://fonts.googleapis.com/css2?family=Yellowtail&family=Nunito:wght@800;900&display=swap" rel="stylesheet">
<style>
  :root {
    --paper: #ffffff;
    --ghost: #f1f1f1;
    --slate: #33495a;
    --slate-deep: #253746;
    --slate-light: #4c6578;
    --script-red: #e0262f;
    --maroon: #642243;
    --ink: #1e1e1e;
    --label: #ffffff;
    --outline: #7f8f9c;
  }
  * { margin: 0; padding: 0; box-sizing: border-box; }
  html, body { width: 927px; height: 1200px; overflow: hidden; background: var(--paper); }
  .cover {
    position: relative;
    width: 927px;
    height: 1200px;
    overflow: hidden;
    background: var(--paper);
    font-family: "Nunito", sans-serif;
  }
  .backdrop { position: absolute; inset: 0; width: 927px; height: 1150px; }
  .ghost-number {
    position: absolute;
    left: -60px;
    top: -40px;
    font-family: "Nunito", sans-serif;
    font-weight: 900;
    font-size: 470px;
    line-height: 1;
    color: var(--ghost);
    letter-spacing: -10px;
  }
  .title-block { position: absolute; left: 40px; top: 100px; }
  .title-script {
    font-family: "Yellowtail", cursive;
    font-size: 92px;
    line-height: 1;
    color: var(--script-red);
    margin-left: 0;
  }
  .title-main {
    font-weight: 900;
    font-size: 84px;
    line-height: 1;
    color: var(--maroon);
    margin-top: -2px;
    margin-left: 8px;
    letter-spacing: -1px;
  }
  .title-ministry {
    font-weight: 900;
    font-size: 44px;
    line-height: 1;
    color: var(--ink);
    margin-top: 16px;
    margin-left: 18px;
  }
  .topics {
    position: absolute;
    left: 57px;
    top: 789px;
    display: flex;
    gap: 18px;
  }
  .topic { width: 194px; text-align: center; }
  .topic-photo {
    width: 194px;
    height: 228px;
    border: 8px solid var(--paper);
    border-radius: 18px;
    background: var(--paper);
    overflow: hidden;
  }
  .topic-photo span { display: block; width: 100%; height: 100%; border-radius: 10px; }
  .photo-evangelism { background: radial-gradient(circle at 50% 45%, #fff3d0 0%, #e8a24a 35%, #6b3a1c 80%); }
  .photo-tongues { background: radial-gradient(circle at 55% 50%, #f5f0ea 0%, #d9531c 35%, #2a0d08 85%); }
  .photo-authority { background: radial-gradient(circle at 50% 50%, #e2b64e 0%, #c8953a 40%, #e6e6e6 72%); }
  .photo-healing { background: linear-gradient(180deg, #6e5f58 0%, #d7894a 60%, #2b1d18 100%); }
  .topic-label {
    margin-top: 18px;
    font-weight: 800;
    font-size: 20px;
    line-height: 1.25;
    color: var(--label);
  }
  .footer {
    position: absolute;
    left: 0;
    top: 1150px;
    width: 927px;
    height: 50px;
    background: var(--paper);
    text-align: center;
    font-weight: 800;
    font-size: 20px;
    line-height: 50px;
    color: var(--ink);
  }
</style>
</head>
<body>
<div class="cover">
  <div class="ghost-number">202</div>

  <svg class="backdrop" viewBox="0 0 927 1150" aria-hidden="true">
    <defs>
      <linearGradient id="slateFill" x1="0" y1="0" x2="0.6" y2="1">
        <stop offset="0" stop-color="#3a5264"/>
        <stop offset="0.55" stop-color="#34495b"/>
        <stop offset="1" stop-color="#2a3c4c"/>
      </linearGradient>
      <radialGradient id="lowGlow" cx="0.15" cy="0.72" r="0.4">
        <stop offset="0" stop-color="#8a4a5a" stop-opacity="0.35"/>
        <stop offset="1" stop-color="#8a4a5a" stop-opacity="0"/>
      </radialGradient>
    </defs>
    <polygon fill="url(#slateFill)" points="
      705,0 927,0 927,1150 60,1150 45,1120 62,1095 30,1070 70,1035 55,1000 95,965
      150,930 190,880 230,840 260,800 300,760 290,730 330,700 345,660 375,630 390,590
      420,560 435,520 470,490 480,450 510,420 520,390 560,360 575,320 600,290 610,250
      640,215 650,180 670,150 665,120 690,90 685,60 705,30">
    </polygon>
    <rect x="0" y="600" width="927" height="550" fill="url(#lowGlow)"/>
    <text x="0" y="0" transform="translate(895 1055) rotate(-90)"
          font-family="Nunito, sans-serif" font-weight="800" font-size="178"
          fill="none" stroke="var(--outline)" stroke-width="3">Stewardship</text>
  </svg>

  <div class="title-block">
    <div class="title-script">Stewardship</div>
    <div class="title-main">Workshop 202</div>
    <div class="title-ministry">Lorna Pell Ministries</div>
  </div>

  <div class="topics">
    <div class="topic">
      <div class="topic-photo"><span class="photo-evangelism" role="img" aria-label="Photo of raised hands reaching toward a glowing cross"></span></div>
      <div class="topic-label">Evangelism</div>
    </div>
    <div class="topic">
      <div class="topic-photo"><span class="photo-tongues" role="img" aria-label="Photo of a white dove in flight before a flaming heart"></span></div>
      <div class="topic-label">Praying in<br>Tongues</div>
    </div>
    <div class="topic">
      <div class="topic-photo"><span class="photo-authority" role="img" aria-label="Photo of a gold officer badge"></span></div>
      <div class="topic-label">Authority of the<br>Believer</div>
    </div>
    <div class="topic">
      <div class="topic-photo"><span class="photo-healing" role="img" aria-label="Silhouette of a man standing with raised arm beside an empty wheelchair at sunset"></span></div>
      <div class="topic-label">Healing</div>
    </div>
  </div>

  <div class="footer">Author: Lorna Pell Ministries</div>
</div>
</body>
</html>
```